Lumo Tavi Menu Design Project

This project is pretty straight forward. You will be given 3 files which include the following:
1. Our proposed menu
2. Our Company logo
3. A sample menu on what we are looking for design wise

Your job is to create a visually pleasing menu that is simple, clean and fresh. Please refer to our home website for additional information. (www.lumotavi.example) Must be in eps or equivalent format.

Target Market(s)

20s to 40s

Industry/Entity Type

It Company

Requirements
Must have
• Company log
Must be in EPS format

```html
<!DOCTYPE html>
<html lang="en">
<head>
<meta charset="utf-8">
<title>Lumo Tavi Menu</title>
<link href="https://fonts.googleapis.com/css2?family=Source+Sans+3:ital,wght@0,400;0,600;0,700;1,400;1,600;1,700&display=swap" rel="stylesheet">
<style>
:root{
  --ink:#1a1a1a;
  --teal:#3fe0bd;
  --teal-dark:#2fcfac;
  --red:#ee1c24;
  --black:#000;
  --paper:#fff;
}
*{box-sizing:border-box;margin:0;padding:0}
html,body{width:927px;height:1200px;overflow:hidden;background:var(--paper)}
body{font-family:"Source Sans 3",sans-serif;color:var(--ink);position:relative}
.menu{position:relative;width:927px;height:1200px}
.item{position:absolute}
.col-left{left:37px;width:416px}
.col-right{left:481px;width:417px}
.item-head{display:flex;justify-content:space-between;align-items:baseline}
.item-name{font-weight:700;font-size:14.5px}
.item-price{font-size:14px;font-weight:400}
.item-desc{font-style:italic;font-size:12.3px;line-height:16.5px;margin-top:2px;max-width:372px}
.section-band{position:absolute;height:36px;background:var(--teal);display:flex;align-items:center;padding-left:6px}
.section-title{color:var(--paper);font-weight:700;font-size:21px;letter-spacing:.3px}
.section-notes{position:absolute;font-style:italic;font-weight:700;font-size:12.3px;line-height:17px}
.footer-band{position:absolute;top:1131px;height:36px}
.footer-band.black{left:0;width:405px;background:var(--black)}
.footer-band.red{left:491px;width:436px;background:var(--red)}
.brand-box{position:absolute;left:405px;top:1100px;width:86px;height:93px;background:var(--paper);border:2px solid var(--black);display:flex;align-items:center;justify-content:center;text-align:center}
.brand-name{font-weight:700;font-size:19px;line-height:20px;color:var(--red)}
</style>
</head>
<body>
<main class="menu">

  <!-- Chicken (continued) -->
  <div class="item col-left" style="top:32px"><div class="item-head"><span class="item-name">Chicken With Snow Peas</span><span class="item-price">11.75</span></div><p class="item-desc">Chicken breast served with snow peas, fresh mushrooms, carrots, and sliced garlic.</p></div>
  <div class="item col-left" style="top:99px"><div class="item-head"><span class="item-name">Teriyaki Chicken Bowl</span><span class="item-price">11.95</span></div><p class="item-desc" style="max-width:400px">Dark meat chicken glazed in Teriyaki sauce placed over a bed of rice.</p></div>
  <div class="item col-left" style="top:150px"><div class="item-head"><span class="item-name">Tangerine Chicken</span><span class="item-price">11.75</span></div><p class="item-desc">Crispy chicken breast topped with scallions in a tangerine sauce.</p></div>
  <div class="item col-left" style="top:200px"><div class="item-head"><span class="item-name">Almond Chicken</span><span class="item-price">11.95</span></div><p class="item-desc">Dark meat chicken with bamboo shoots, celery, water chestnuts, and toasted almonds. Prepared regularly or mandarin-Style.</p></div>
  <div class="item col-left" style="top:268px"><div class="item-head"><span class="item-name">Lemon Chicken</span><span class="item-price">11.75</span></div><p class="item-desc" style="max-width:350px">Crispy chicken breast marinated in garlic and ginger; served with a tart lemon sauce on the side.</p></div>
  <div class="item col-left" style="top:335px"><div class="item-head"><span class="item-name">Cashew Chicken</span><span class="item-price">11.95</span></div><p class="item-desc">Chicken breast, zucchini, onions, garlic, ginger, and cashews tossed n an oyster sauce.</p></div>
  <div class="item col-left" style="top:402px"><div class="item-head"><span class="item-name">Curry Chicken</span><span class="item-price">11.95</span></div><p class="item-desc">Chicken breast with potatoes, onions, green peas, and carrots in a curry sauce.</p></div>
  <div class="item col-left" style="top:470px"><div class="item-head"><span class="item-name">Sweet And Sour Chicken</span><span class="item-price">11.50</span></div><p class="item-desc" style="max-width:345px">Crispy chicken breast, bell peppers, onions, and pineapple in a sweet and sour sauce.</p></div>

  <!-- Beef & Pork -->
  <div class="section-band" style="left:34px;top:535px;width:422px"><h2 class="section-title">BEEF &amp; PORK</h2></div>
  <div class="section-notes" style="left:37px;top:574px">Rice is not included. Add rice $1.25.<br>Enjoy a Half Chinese Chicken Salad or Plain Fried Rice with<br>any entrée for $5.50<br>Can replace Beef/Pork with Tofu for $1.50</div>

  <div class="item col-left" style="top:658px"><div class="item-head"><span class="item-name">Mongolian Beef</span><span class="item-price">12.25</span></div><p class="item-desc" style="max-width:360px">Flank steak, garlic, ginger, and green onions on a bed of white crunchies.</p></div>
  <div class="item col-left" style="top:725px"><div class="item-head"><span class="item-name">Beef And Broccoli</span><span class="item-price">11.95</span></div><p class="item-desc" style="max-width:360px">Flank steak, broccoli, and black mushrooms sautéed in a garlic brown sauce.</p></div>
  <div class="item col-left" style="top:792px"><div class="item-head"><span class="item-name">Pepper Steak</span><span class="item-price">11.95</span></div><p class="item-desc" style="max-width:410px">Flank steak, bell peppers, onions, and garlic in black pepper sauce.</p></div>
  <div class="item col-left" style="top:859px"><div class="item-head"><span class="item-name">Sliced Barbequed Pork</span><span class="item-price">8.95</span></div><p class="item-desc" style="max-width:410px">Tender slices of juicy pork topped with scallions in a barbeque sauce.</p></div>
  <div class="item col-left" style="top:909px"><div class="item-head"><span class="item-name">Barbequed Spareribs</span><span class="item-price">8.95</span></div><p class="item-desc">Slow-Roasted juicy pork ribs with barbeque sauce.</p></div>
  <div class="item col-left" style="top:960px"><div class="item-head"><span class="item-name">Tangerine Beef</span><span class="item-price">12.25</span></div><p class="item-desc">Crisp flank steak topped with scallions in a tangerine sauce.</p></div>
  <div class="item col-left" style="top:1010px"><div class="item-head"><span class="item-name">Spicy Garlic Tomato Beef</span><span class="item-price">12.95</span></div><p class="item-desc" style="max-width:360px">Flank steak, tomato, water chestnuts, zucchini, onions, and spicy garlic sauce.</p></div>
  <div class="item col-left" style="top:1065px"><div class="item-head"><span class="item-name">Ma Pao Tofu</span><span class="item-price">7.95</span></div><p class="item-desc" style="max-width:360px">Soft tofu cubes with ground pork or chicken cooked in Szechuan-Style sauce.</p></div>

  <!-- Seafood -->
  <div class="section-band" style="left:479px;top:23px;width:425px"><h2 class="section-title">SEAFOOD</h2></div>
  <div class="section-notes" style="left:481px;top:63px">Enjoy a Half Chinese Chicken Salad or Plain Fried Rice with<br>any entrée for $5.50<br>Can replace Seafood with Tofu for $1.50</div>

  <div class="item col-right" style="top:145px"><div class="item-head"><span class="item-name">Crispy Spicy Honey Shrimp</span><span class="item-price">13.95</span></div><p class="item-desc">Crispy large shrimp with red bell peppers, scallions, and chili peppers in a sweet honey sauce.</p></div>
  <div class="item col-right" style="top:212px"><div class="item-head"><span class="item-name">Kung Pao Three Treasures</span><span class="item-price">13.95</span></div><p class="item-desc">Large shrimp, beef, and chicken breast with scallions, peanuts, water chestnuts, and chili peppers. Prepared mandarin-Style.</p></div>
  <div class="item col-right" style="top:280px"><div class="item-head"><span class="item-name">Honey Walnut Shrimp</span><span class="item-price">13.95</span></div><p class="item-desc">Lightly crisped savory shrimp with honey-Glazed walnuts.</p></div>
  <div class="item col-right" style="top:331px"><div class="item-head"><span class="item-name">Fish With Ginger Soy Sauce</span><span class="item-price">15.95</span></div><p class="item-desc" style="max-width:360px">Whole white fish filet steamed with ginger and topped with green onions and cilantro.</p></div>
  <div class="item col-right" style="top:398px"><div class="item-head"><span class="item-name">Shrimp With Snow Peas</span><span class="item-price">13.95</span></div><p class="item-desc">Large shrimp with snow peas, water chestnuts, carrots, and ginger in a white wine sauce.</p></div>
  <div class="item col-right" style="top:465px"><div class="item-head"><span class="item-name">Shrimp With Lobster Sauce</span><span class="item-price">13.95</span></div><p class="item-desc">Large shrimp, eggs, ground pork, snow peas, water chestnuts, and red bell peppers sautéed in a lobster sauce.</p></div>
  <div class="item col-right" style="top:532px"><div class="item-head"><span class="item-name">Salt And Pepper Shrimp</span><span class="item-price">13.95</span></div><p class="item-desc" style="max-width:360px">Lightly battered large shrimp with a pepper spice; served with bell peppers and white crunchies.</p></div>
  <div class="item col-right" style="top:600px"><div class="item-head"><span class="item-name">Cashew Shrimp</span><span class="item-price">13.95</span></div><p class="item-desc" style="max-width:360px">Large shrimp with zucchini, onions, and roasted cashews in oyster sauce.</p></div>
  <div class="item col-right" style="top:666px"><div class="item-head"><span class="item-name">Orange Shrimp</span><span class="item-price">13.95</span></div><p class="item-desc">Large crispy shrimp with onions and red and green bell peppers in a sweet orange sauce.</p></div>

  <!-- Vegetables -->
  <div class="section-band" style="left:479px;top:741px;width:425px"><h2 class="section-title">VEGETABLES</h2></div>
  <div class="section-notes" style="left:481px;top:779px">Enjoy a Half Chinese Chicken Salad or Plain Fried Rice<br>with any entrée for $5.50<br>Can add Tofu for $1.50</div>

  <div class="item col-right" style="top:846px"><div class="item-head"><span class="item-name">Fragrant Vegetables</span><span class="item-price">8.95</span></div><p class="item-desc" style="max-width:340px">Mixed vegetables with white wine, curry, garlic, black bean, kungpao, or vegetarian sauce.</p></div>
  <div class="item col-right" style="top:913px"><div class="item-head"><span class="item-name">Vegetable Lettuce Wraps</span><span class="item-price">9.95</span></div><p class="item-desc" style="max-width:360px">Black mushrooms, bell peppers, water chestnuts, smoked tofu, pine nuts, and white crunchies. Served with four lettuce cups.</p></div>
  <div class="item col-right" style="top:980px"><div class="item-head"><span class="item-name">Szechuan String Beans</span><span class="item-price">8.95</span></div><p class="item-desc" style="max-width:360px">Blue lake green beans and garlic sautéed with pickled szechwan vegetables.</p></div>
  <div class="item col-right" style="top:1048px"><div class="item-head"><span class="item-name">Tofu With Black Mushrooms</span><span class="item-price">7.95</span></div><p class="item-desc" style="max-width:340px">Fried tofu triangles sautéed with scallions, black mushrooms, water chestnuts, and cabbage.</p></div>

  <!-- Footer -->
  <div class="footer-band black"></div>
  <div class="footer-band red"></div>
  <div class="brand-box"><span class="brand-name">Lumo<br>Tavi</span></div>

</main>
</body>
</html>
```